Artwork flyer ( named LU MO RAY ) for my music festival

I need a flyer artwork created for my indie pop, rock, hip-hop and dance music festival as soon as possible. The festival is for ages 18 to 30. Need flyer to be able to be abstracted so i can export into different social media
sizes etc

Here is some information around the music festival details.

Title: LU MO RAY ( music festival)

Artists :
KIRO Fen
Mirela Post
TRGs
The Brindles
Zank Pods
Velvet Otter
Copper ah
Quiet Tundra

Venue: Harrowmere Paddock Club
Date: Saturday 25th March
Tickets: www.tikvarro.com.au

Logo Text

LUMO RAY ( or LU MO RAY)

```html
<!DOCTYPE html>
<html lang="en">
<head>
<meta charset="utf-8">
<title>LU MO RAY – Music Festival Flyer</title>
<link href="https://fonts.googleapis.com/css2?family=Barlow+Condensed:wght@300;400;600;700;800&family=Michroma&family=Poppins:wght@700&display=swap" rel="stylesheet">
<style>
  :root {
    --backdrop: #b4b4b4;
    --ink: #0a0a0a;
    --paper: #ffffff;
    --mid-grey: #6b6b6b;
    --soft-grey: #9a9a9a;
    --light-grey: #d8d8d8;
  }
  * { margin: 0; padding: 0; box-sizing: border-box; }
  html, body {
    width: 750px; height: 1200px; overflow: hidden;
    background: var(--backdrop);
  }
  .flyer {
    position: absolute; left: 0; top: 69px;
    width: 750px; height: 1062px;
    background: var(--ink);
    overflow: hidden;
    box-shadow: 0 6px 14px rgba(0,0,0,.35);
    font-family: "Barlow Condensed", sans-serif;
    color: var(--paper);
  }
  .art { position: absolute; display: block; }
  .art--ribbons { left: 0; top: 0; width: 750px; height: 520px; }
  .art--notes { left: 560px; top: 470px; width: 190px; height: 140px; }
  .art--listener { left: 0; top: 0; width: 750px; height: 1062px; }

  .title { position: absolute; left: 58px; top: 205px; width: 640px; height: 280px; }
  .title__word, .title__echo {
    position: absolute; left: 0; top: 0;
    font-weight: 800; font-size: 176px; line-height: 1;
    letter-spacing: 2px; white-space: nowrap;
  }
  .title__word { color: var(--paper); }
  .title__echo { color: transparent; -webkit-text-stroke: 1px var(--soft-grey); }
  .title__echo--1 { top: 26px; opacity: .8; }
  .title__echo--2 { top: 52px; opacity: .55; }
  .title__echo--3 { top: 78px; opacity: .3; }

  .date { position: absolute; left: 63px; top: 500px; width: 320px; height: 200px; }
  .date__day { position: absolute; left: 0; top: 6px; font-weight: 700; font-size: 40px; line-height: 1; color: var(--light-grey); }
  .date__month {
    position: absolute; left: 0; top: 48px; width: 150px; height: 46px;
    border: 1.5px solid var(--soft-grey);
    font-weight: 300; font-size: 40px; line-height: 44px; letter-spacing: 4px;
    text-align: center; color: var(--light-grey);
  }
  .date__num { position: absolute; left: 158px; top: -10px; font-weight: 800; font-size: 118px; line-height: 1; }
  .date__suffix { position: absolute; left: 274px; top: 2px; font-weight: 300; font-size: 34px; line-height: 1; }
  .date__year { position: absolute; left: 0; top: 104px; font-family: "Michroma", sans-serif; font-size: 74px; line-height: 1; color: var(--soft-grey); }

  .lineup { position: absolute; left: 64px; top: 718px; }
  .lineup__heading { font-weight: 300; font-size: 27px; line-height: 1; margin-bottom: 20px; }
  .lineup__heading strong { font-weight: 700; }
  .lineup__list { list-style: none; }
  .lineup__item { font-size: 16px; letter-spacing: 1px; line-height: 29.5px; text-transform: uppercase; color: var(--light-grey); }

  .venue { position: absolute; right: 62px; top: 780px; text-align: right; color: var(--ink); }
  .venue__at { font-weight: 700; font-size: 30px; line-height: 1; }
  .venue__name { font-weight: 700; font-size: 50px; line-height: .95; color: var(--mid-grey); margin-top: 4px; }
  .venue__place { font-size: 50px; line-height: 1; }
  .venue__place strong { font-weight: 700; }
  .venue__place span { font-weight: 300; }

  .tickets { position: absolute; right: 62px; top: 955px; text-align: right; color: var(--ink); }
  .tickets__label { font-weight: 400; font-size: 15px; letter-spacing: 4px; color: var(--mid-grey); }
  .tickets__url { font-family: "Poppins", sans-serif; font-weight: 700; font-size: 22px; line-height: 1.3; }
</style>
</head>
<body>
  <main class="flyer">
    <svg class="art art--listener" role="img" aria-label="White silhouette of a listener's head in profile" viewBox="0 0 750 1062">
      <path d="M290 1062 V760 C290 660 400 605 520 600 C620 596 710 620 750 640 V1062 Z" fill="var(--paper)"/>
    </svg>

    <svg class="art art--ribbons" role="img" aria-label="Black and white op-art striped ribbons flowing across the top and down the left edge" viewBox="0 0 750 520">
      <defs>
        <linearGradient id="ribbonTone" x1="0" y1="0" x2="1" y2="1">
          <stop offset="0" stop-color="#e6e6e6"/>
          <stop offset=".5" stop-color="#8c8c8c"/>
          <stop offset="1" stop-color="#2a2a2a"/>
        </linearGradient>
      </defs>
      <path d="M0 0 H750 V150 C620 160 520 230 420 225 C300 220 200 170 120 200 C80 220 70 300 70 400 L40 520 H0 Z" fill="url(#ribbonTone)"/>
    </svg>

    <svg class="art art--notes" role="img" aria-label="Scattered white music notes rising above the listener's head" viewBox="0 0 190 140">
      <defs>
        <radialGradient id="notesTone" cx=".5" cy=".5" r=".5">
          <stop offset="0" stop-color="#3a3a3a"/>
          <stop offset="1" stop-color="#0a0a0a"/>
        </radialGradient>
      </defs>
      <rect x="0" y="0" width="190" height="140" fill="url(#notesTone)"/>
    </svg>

    <h1 class="title" aria-label="LU MO RAY">
      <span class="title__echo title__echo--3" aria-hidden="true">LU MO RAY</span>
      <span class="title__echo title__echo--2" aria-hidden="true">LU MO RAY</span>
      <span class="title__echo title__echo--1" aria-hidden="true">LU MO RAY</span>
      <span class="title__word">LU MO RAY</span>
    </h1>

    <section class="date">
      <span class="date__day">SATURDAY</span>
      <span class="date__month">MARCH</span>
      <span class="date__num">25</span>
      <span class="date__suffix">TH</span>
      <span class="date__year">2023</span>
    </section>

    <section class="lineup">
      <h2 class="lineup__heading">PERFORMING <strong>ARTISTS</strong></h2>
      <ul class="lineup__list">
        <li class="lineup__item">KIRO Fen</li>
        <li class="lineup__item">Mirela Post</li>
        <li class="lineup__item">TRGs</li>
        <li class="lineup__item">The Brindles</li>
        <li class="lineup__item">Zank Pods</li>
        <li class="lineup__item">Velvet Otter</li>
        <li class="lineup__item">Copper ah</li>
        <li class="lineup__item">Quiet Tundra</li>
      </ul>
    </section>

    <section class="venue">
      <p class="venue__at">AT</p>
      <p class="venue__name">HARROWMERE</p>
      <p class="venue__place"><strong>PADDOCK</strong> <span>CLUB</span></p>
    </section>

    <section class="tickets">
      <p class="tickets__label">BOOK YOUR TICKETS</p>
      <p class="tickets__url">www.tikvarro.com.au</p>
    </section>
  </main>
</body>
</html>
```